Business Card Design Project

I want my business cards to stand and feel timeless! I also want people to get their hands on them and freak out over how cool these are, I already have a logo i just want a very cool card design! this is for a makeup artist and maybe one day a line of cosmetics.

Target Market(s)

I want this to target women from 18 to 45

Industry/Entity Type

Business

Font styles to use
Decorative
Script

Colors

Designer to choose colors to be used in the design.

Requirements
Must have
• it must be elegante

```html
<!DOCTYPE html>
<html lang="en">
<head>
<meta charset="utf-8">
<title>Marisette – Business Cards</title>
<link rel="stylesheet" href="https://fonts.googleapis.com/css2?family=Lobster&family=Poiret+One&display=swap">
<style>
  :root {
    --backdrop: #262626;
    --card-dark: #1f1c1d;
    --card-light: #eceeed;
    --band: #e2e3e2;
    --ink-logo: #2a2a2a;
    --ink-blue: #3d3a9a;
    --ink-orange: #f39a1e;
    --line-pink: #f4c2d8;
    --line-lilac: #a884c9;
    --line-blue: #3c35a8;
  }
  * { margin: 0; padding: 0; box-sizing: border-box; }
  html, body { width: 1200px; height: 800px; overflow: hidden; }
  body {
    background: var(--backdrop);
    display: flex;
    align-items: center;
    justify-content: center;
    gap: 60px;
  }
  .card {
    position: relative;
    width: 525px;
    height: 300px;
    border-radius: 3px;
    overflow: hidden;
    box-shadow: 0 14px 30px rgba(0,0,0,.45);
  }

  /* Back of card */
  .card--back { background: var(--card-dark); }
  .card--back .band {
    position: absolute;
    left: 0; right: 0;
    top: 90px;
    height: 92px;
    background: var(--band);
    display: flex;
    align-items: center;
    justify-content: center;
  }
  .wordmark {
    font-family: "Poiret One", sans-serif;
    font-weight: 400;
    color: var(--ink-logo);
    letter-spacing: 0.08em;
    text-transform: uppercase;
    line-height: 1;
  }
  .card--back .wordmark { font-size: 48px; }
  .card--back .accent-line {
    position: absolute;
    left: 0;
    top: 236px;
    width: 230px;
    height: 5px;
    background: linear-gradient(90deg, var(--line-pink) 0%, rgba(244,194,216,.55) 70%, rgba(244,194,216,0) 100%);
  }

  /* Front of card */
  .card--front { background: var(--card-light); }
  .contact-block {
    position: absolute;
    right: 40px;
    top: 48px;
    width: 300px;
    text-align: right;
  }
  .person-name {
    font-family: "Lobster", cursive;
    font-size: 27px;
    line-height: 1;
  }
  .person-name .first { color: var(--ink-blue); }
  .person-name .last { color: var(--ink-orange); }
  .person-role {
    font-family: "Lobster", cursive;
    color: var(--ink-orange);
    font-size: 18px;
    margin-top: 2px;
    margin-right: 40px;
  }
  .card--front .wordmark {
    font-size: 36px;
    margin-top: 6px;
    text-align: left;
    margin-left: 20px;
  }
  .contact-line {
    font-family: "Lobster", cursive;
    color: var(--ink-orange);
    font-size: 17px;
    letter-spacing: 0.04em;
    display: flex;
    align-items: center;
    justify-content: flex-end;
    gap: 8px;
    margin-top: 8px;
  }
  .contact-line svg { width: 14px; height: 14px; flex: none; }
  .card--front .accent-line {
    position: absolute;
    left: 0; right: 0;
    top: 196px;
    height: 7px;
    background: linear-gradient(90deg, var(--line-pink) 0%, var(--line-lilac) 60%, var(--line-blue) 100%);
  }
</style>
</head>
<body>
  <section class="card card--back" aria-label="Card back">
    <div class="band">
      <span class="wordmark">Marisette</span>
    </div>
    <div class="accent-line"></div>
  </section>

  <section class="card card--front" aria-label="Card front">
    <div class="contact-block">
      <p class="person-name"><span class="first">Clara</span> <span class="last">Bennett</span></p>
      <p class="person-role">CEO</p>
      <p class="wordmark">Marisette</p>
      <p class="contact-line">00 987 654 321
        <svg viewBox="0 0 14 14" aria-hidden="true">
          <rect x="3.5" y="0.8" width="7" height="12.4" rx="1.4" fill="none" stroke="#3d3a9a" stroke-width="1.2"/>
          <line x1="6" y1="11" x2="8" y2="11" stroke="#3d3a9a" stroke-width="1.2"/>
        </svg>
      </p>
      <p class="contact-line">www.bennett.com
        <svg viewBox="0 0 14 14" aria-hidden="true">
          <circle cx="7" cy="7" r="6" fill="#3d3a9a"/>
        </svg>
      </p>
    </div>
    <div class="accent-line"></div>
  </section>
</body>
</html>
```